TALL WAVE

I am in this industry for last 15 years we have done lots of commercial site like we work with ORBEL costruction, loam properties, DRV, quill construction.
We do all domestic and commercial wall and floor tiling, swimming pools, spas, paving, marbles blue stones and muchmore.

Specializing in the wall and floor Tiling, Waterproofing and floor preparations

Industry/Entity Type

Industry

Number of Pages Required

1 page

Font styles to use
Serif
Decorative

Colors

Designer to choose colors to be used in the design.

Requirements
Must have
• domestic and commercial indoor tiling, bathroom tiling and paving pictures
Nice to have
• beautiful bathroom pictures with tile

```html
<!DOCTYPE html>
<html lang="en">
<head>
<meta charset="utf-8">
<title>Tall Wave Construction</title>
<link href="https://fonts.googleapis.com/css2?family=Exo+2:wght@700;800&family=Lato:wght@400;700;900&family=Oswald:wght@400&display=swap" rel="stylesheet">
<style>
:root{
  --blue:#0b4f7f;
  --blue-dark:#08406a;
  --grey:#8b8e92;
  --grey-btn:#7d8084;
  --ink:#222;
  --text:#444;
  --light:#efefef;
  --footer:#2f2f2f;
  --white:#fff;
}
*{box-sizing:border-box;margin:0;padding:0}
html,body{width:1200px;height:2995px;overflow:hidden;background:var(--white)}
body{font-family:"Lato",sans-serif;color:var(--text);position:relative}
.photo{position:absolute}

/* header */
.site-header{position:absolute;left:0;top:0;width:1200px;height:128px;border-top:3px solid var(--blue-dark);background:var(--white)}
.brand{position:absolute;left:96px;top:20px;width:140px;text-align:center}
.brand-mark{display:block;margin:0 auto 4px;width:34px;height:34px;background:var(--blue)}
.brand-name{font-family:"Lato",sans-serif;font-weight:900;font-size:25px;color:var(--blue);line-height:1}
.brand-sub{font-family:"Lato",sans-serif;font-weight:900;font-size:13px;color:var(--blue);letter-spacing:1px;margin-top:3px}
.top-contact{position:absolute;top:20px;left:598px;display:flex;align-items:center;gap:10px;font-size:17px;color:#555}
.ico-round{width:28px;height:28px;border-radius:50%;background:var(--blue);display:inline-flex;align-items:center;justify-content:center}
.top-contact .gap{width:22px}
.socials{display:flex;gap:8px;margin-left:16px}
.socials span{width:30px;height:30px;border-radius:50%;background:var(--blue)}
.socials span:nth-child(2){background:#2a8fc7}
.socials span:nth-child(4){background:#b8322b}
.main-nav{position:absolute;top:82px;left:454px;display:flex;font-weight:700;font-size:15.5px;letter-spacing:.6px;color:#555}
.main-nav a{color:#555;text-decoration:none;margin-right:52px}
.main-nav a.active{color:var(--blue)}

/* hero */
.hero{position:absolute;left:0;top:128px;width:1200px;height:514px;background:linear-gradient(90deg,#6b5446 0%,#8d8f91 22%,#a6a7a8 45%,#d9d8d4 70%,#eceae6 100%)}
.hero-caption{position:absolute;left:0;width:1200px;top:452px;text-align:center;font-family:"Oswald",sans-serif;font-size:32px;color:var(--white);text-shadow:0 2px 4px rgba(0,0,0,.5)}
.hero-arrow{position:absolute;top:216px;width:36px;height:34px;background:rgba(20,20,20,.75);display:flex;align-items:center;justify-content:center}

/* sectors */
.sectors{position:absolute;top:642px;left:0;width:1200px;height:134px;display:flex}
.sector{flex:1;position:relative;color:var(--white)}
.sector.domestic{background:var(--grey)}
.sector.commercial{background:var(--blue)}
.sector-ico{position:absolute;top:15px;width:104px;height:104px;border-radius:50%;display:flex;align-items:center;justify-content:center}
.domestic .sector-ico{left:98px;background:var(--blue)}
.commercial .sector-ico{left:40px;background:var(--grey)}
.sector h3{position:absolute;top:24px;font-family:"Exo 2",sans-serif;font-weight:800;font-size:19px;letter-spacing:.5px}
.sector p{position:absolute;top:52px;width:340px;font-size:13.5px;line-height:20px}
.domestic h3,.domestic p{left:236px}
.commercial h3,.commercial p{left:178px}

/* headings */
.section-title{position:absolute;left:0;width:1200px;text-align:center;font-family:"Exo 2",sans-serif;font-weight:800;font-size:31px;letter-spacing:.6px;color:var(--blue)}
.section-title .soft{color:var(--grey)}
.divider{position:absolute;left:515px;width:170px;height:22px}
.btn{position:absolute;height:34px;background:var(--grey-btn);color:var(--white);font-weight:900;font-size:12.5px;letter-spacing:.8px;display:flex;align-items:center;justify-content:center}

/* about */
.about-text{position:absolute;left:100px;top:902px;width:1000px;text-align:center;font-size:12.6px;line-height:24px;color:#444}

/* specializing */
.specials{position:absolute;top:1106px;left:0;width:1200px;height:614px;background:var(--light)}
.card{position:absolute;top:148px;width:316px;height:412px;background:var(--white);border:1px solid #ddd;border-bottom:4px solid var(--blue)}
.card .photo{left:4px;top:4px;width:306px;height:186px}
.card-ico{position:absolute;left:124px;top:160px;width:66px;height:66px;border-radius:50%;background:var(--blue);border:3px solid var(--white);display:flex;align-items:center;justify-content:center}
.card h4{position:absolute;top:240px;left:0;width:100%;text-align:center;font-family:"Exo 2",sans-serif;font-weight:800;font-size:19px;color:var(--ink);letter-spacing:.5px}
.card p{position:absolute;top:274px;left:30px;width:254px;text-align:center;font-size:13.5px;line-height:21px;color:#333}
.card .btn{left:94px;top:346px;width:126px}

/* work */
.tile{position:absolute;overflow:hidden}
.tile-label{position:absolute;left:0;bottom:0;width:100%;height:36px;background:rgba(60,60,60,.55);color:var(--white);font-size:13px;font-weight:700;letter-spacing:.5px;display:flex;align-items:center;justify-content:center}

/* partners */
.partners{position:absolute;top:2354px;left:0;width:1200px;height:306px;background:var(--light)}
.partner{position:absolute;top:140px;width:214px;height:120px;background:var(--white);border:1px solid #d6d6d6;display:flex;align-items:center;justify-content:center;gap:10px;font-family:"Lato",sans-serif;font-weight:700;font-size:24px;color:#444}
.partner .dot{width:22px;height:22px;background:#444}
.partner .dot.round{border-radius:50%}

/* footer */
.site-footer{position:absolute;top:2660px;left:0;width:1200px;height:295px;background:var(--footer);color:#ddd}
.foot-h{position:absolute;top:42px;font-weight:900;font-size:16px;letter-spacing:1px;color:var(--white)}
.quick{position:absolute;left:100px;top:90px;list-style:none;font-size:13.5px;line-height:30px}
.quick li::before{content:"»";margin-right:14px;color:#bbb}
.contact{position:absolute;left:320px;top:90px;font-size:13.5px;line-height:20px;width:280px}
.contact .row{display:flex;gap:12px;margin-bottom:10px;align-items:flex-start}
.contact svg{flex:none;margin-top:2px}
.contact strong{color:var(--white);font-weight:900}
.map{position:absolute;left:630px;top:94px;width:236px;height:146px;border:3px solid #ddd;background:linear-gradient(135deg,#bcd6a8,#e6e2cf 55%,#d7dfc4)}
.foot-brand{position:absolute;left:960px;top:100px;width:140px;text-align:center;color:var(--white)}
.foot-brand .brand-mark{background:#ccc}
.foot-brand .brand-name,.foot-brand .brand-sub{color:var(--white)}
.foot-socials{display:flex;gap:8px;justify-content:center;margin-top:12px}
.foot-socials span{width:28px;height:28px;border-radius:50%;background:#2a8fc7}
.foot-socials span:first-child{background:var(--blue)}
.foot-socials span:last-child{background:#b8322b}
.copyright{position:absolute;top:2955px;left:0;width:1200px;height:40px;background:var(--blue-dark);color:#e6e6e6;font-size:13px;display:flex;align-items:center;justify-content:center}
</style>
</head>
<body>

<header class="site-header">
  <div class="brand">
    <span class="brand-mark"></span>
    <div class="brand-name">Tall Wave</div>
    <div class="brand-sub">CONSTRUCTION</div>
  </div>
  <div class="top-contact">
    <span class="ico-round"><svg width="14" height="14" viewBox="0 0 24 24"><path fill="#fff" d="M6.6 10.8a15 15 0 0 0 6.6 6.6l2.2-2.2c.3-.3.7-.4 1-.2 1.1.4 2.3.6 3.6.6.6 0 1 .4 1 1V20c0 .6-.4 1-1 1A17 17 0 0 1 3 4c0-.6.4-1 1-1h3.5c.6 0 1 .4 1 1 0 1.3.2 2.5.6 3.6.1.3 0 .7-.2 1z"/></svg></span>
    <span>555-014-2290</span>
    <span class="gap"></span>
    <span class="ico-round"><svg width="14" height="14" viewBox="0 0 24 24"><path fill="#fff" d="M2 5h20v14H2zm2 2v.5l8 5 8-5V7l-8 5z"/></svg></span>
    <span>hello@tallwave.example</span>
    <div class="socials"><span></span><span></span><span></span><span></span></div>
  </div>
  <nav class="main-nav">
    <a class="active">HOME</a><a>ABOUT US</a><a>SERVICES</a><a>OUR WORK</a><a>CONTACT US</a>
  </nav>
</header>

<section class="hero" role="img" aria-label="Bright bathroom with a grey stone tiled feature wall, freestanding tub and timber stairs">
  <div class="hero-arrow" style="left:0"><svg width="12" height="14" viewBox="0 0 12 14"><path d="M9 1 3 7l6 6" stroke="#fff" stroke-width="2.5" fill="none"/></svg></div>
  <div class="hero-arrow" style="right:0"><svg width="12" height="14" viewBox="0 0 12 14"><path d="m3 1 6 6-6 6" stroke="#fff" stroke-width="2.5" fill="none"/></svg></div>
  <div class="hero-caption">Specializing In The Wall And Floor Tiling, Waterproofing And Floor Preparations</div>
</section>

<section class="sectors">
  <div class="sector domestic">
    <div class="sector-ico"><svg width="54" height="48" viewBox="0 0 54 48"><path d="M27 4 3 24h7v20h12V32h10v12h12V24h7z" fill="#fff"/></svg></div>
    <h3>DOMESTIC</h3>
    <p>Lorem ipsum dolor sit amet, consectetuer adipiscing elit, sed diam nonummy nibh euismod tincidunt ut laoreet dolore magna aliquam erat...[+]</p>
  </div>
  <div class="sector commercial">
    <div class="sector-ico"><svg width="44" height="50" viewBox="0 0 44 50"><path d="M6 4h32v44H6z" fill="#fff"/><g fill="#8b8e92"><rect x="11" y="9" width="6" height="6"/><rect x="19" y="9" width="6" height="6"/><rect x="27" y="9" width="6" height="6"/><rect x="11" y="19" width="6" height="6"/><rect x="19" y="19" width="6" height="6"/><rect x="27" y="19" width="6" height="6"/><rect x="11" y="29" width="6" height="6"/><rect x="27" y="29" width="6" height="6"/><rect x="18" y="38" width="8" height="10"/></g></svg></div>
    <h3>COMMERCIAL</h3>
    <p>Lorem ipsum dolor sit amet, consectetuer adipiscing elit, sed diam nonummy nibh euismod tincidunt ut laoreet dolore magna aliquam erat...[+]</p>
  </div>
</section>

<h2 class="section-title" style="top:818px">ABOUT TALL WAVE <span class="soft">CONSTRUCTION</span></h2>
<svg class="divider" style="top:862px" viewBox="0 0 170 22"><line x1="0" y1="11" x2="70" y2="11" stroke="#bbb"/><line x1="100" y1="11" x2="170" y2="11" stroke="#bbb"/><path d="M78 18h14V8l-7-5-7 5z" fill="var(--blue)"/></svg>
<p class="about-text">Lorem ipsum dolor sit amet, consectetuer adipiscing elit, sed diam nonummy nibh euismod tincidunt ut laoreet dolore magna aliquam erat volutpat. Ut wisi enim ad minim veniam, quis nostrud exerci tation ullamcorper suscipit lobortis nisl ut aliquip ex ea commodo consequat. Duis autem vel eum iriure dolor in hendrerit in vulputate velit esse molestie consequat, vel illum dolore eu feugiat nulla facilisis at vero eros et accumsan et iusto odio dignissim qui blandit praesent luptatum zzril delenit augue duis dolore te feugait nulla facilisi.nibh euismod tincidunt ut laoreet dolore magna aliquam erat volutpat.</p>
<div class="btn" style="left:538px;top:1024px;width:124px">READ MORE</div>

<section class="specials">
  <h2 class="section-title" style="top:46px">WE SPECIALIZING <span class="soft">IN</span></h2>
  <svg class="divider" style="top:90px" viewBox="0 0 170 22"><line x1="0" y1="11" x2="70" y2="11" stroke="#bbb"/><line x1="100" y1="11" x2="170" y2="11" stroke="#bbb"/><path d="M78 18h14V8l-7-5-7 5z" fill="var(--blue)"/></svg>

  <article class="card" style="left:100px">
    <div class="photo" role="img" aria-label="Tiler fixing white wall tiles" style="background:linear-gradient(135deg,#d8d2c8,#9a8f84 60%,#6d645c)"></div>
    <div class="card-ico"><svg width="30" height="30" viewBox="0 0 30 30"><path d="M15 3 27 15 15 27 3 15z" fill="none" stroke="#fff" stroke-width="2.5"/><path d="M15 9 21 15 15 21 9 15z" fill="#fff"/></svg></div>
    <h4>WALL AND FLOOR TILING</h4>
    <p>Lorem ipsum dolor sit amet, consectetur adipiscing elit. Praesent vestibulum velit felis. Maecenas ac faucibus turpis.</p>
    <div class="btn">READ MORE</div>
  </article>
  <article class="card" style="left:442px">
    <div class="photo" role="img" aria-label="Workers applying waterproofing membrane on a city rooftop" style="background:linear-gradient(180deg,#b9c3cc,#8c949a 45%,#2f3337)"></div>
    <div class="card-ico"><svg width="32" height="30" viewBox="0 0 32 30"><path d="M3 26 18 11" stroke="#fff" stroke-width="3"/><path d="M20 4l2 4 4 2-4 2-2 4-2-4-4-2 4-2z" fill="#fff"/></svg></div>
    <h4>WATERPROOFING</h4>
    <p>Lorem ipsum dolor sit amet, consectetur adipiscing elit. Praesent vestibulum velit felis. Maecenas ac faucibus turpis.</p>
    <div class="btn">READ MORE</div>
  </article>
  <article class="card" style="left:788px">
    <div class="photo" role="img" aria-label="Crew in safety vests preparing a concrete floor" style="background:linear-gradient(135deg,#a89a8a,#6f655c 55%,#4a4440)"></div>
    <div class="card-ico"><svg width="28" height="30" viewBox="0 0 28 30"><rect x="3" y="4" width="18" height="23" fill="none" stroke="#fff" stroke-width="2.5"/><path d="M12 20 24 6" stroke="#fff" stroke-width="3"/></svg></div>
    <h4>FLOOR PREPARATIONS</h4>
    <p>Lorem ipsum dolor sit amet, consectetur adipiscing elit. Praesent vestibulum velit felis. Maecenas ac faucibus turpis.</p>
    <div class="btn">READ MORE</div>
  </article>
</section>

<h2 class="section-title" style="top:1756px">OUR <span class="soft">WORK</span></h2>
<svg class="divider" style="top:1800px" viewBox="0 0 170 22"><line x1="0" y1="11" x2="70" y2="11" stroke="#bbb"/><line x1="100" y1="11" x2="170" y2="11" stroke="#bbb"/><path d="M78 18h14V8l-7-5-7 5z" fill="var(--blue)"/></svg>

<div class="tile" style="left:100px;top:1858px;width:236px;height:182px">
  <div class="photo" role="img" aria-label="Indoor spa pool with mosaic tiled wall" style="inset:0;background:linear-gradient(160deg,#c5a77f,#8e7457 50%,#6fa6a8)"></div>
  <div class="tile-label">SPAS</div>
</div>
<div class="tile" style="left:356px;top:1858px;width:236px;height:182px">
  <div class="photo" role="img" aria-label="Backyard swimming pool at dusk" style="inset:0;background:linear-gradient(160deg,#3d5a4a,#2a3c44 60%,#1f2a33)"></div>
  <div class="tile-label">SWIMMING POOLS</div>
</div>
<div class="tile" style="left:610px;top:1858px;width:236px;height:380px">
  <div class="photo" role="img" aria-label="Curved paver garden path between green plants" style="inset:0;background:linear-gradient(180deg,#6f9a3f,#b9b4a6 45%,#9c978b)"></div>
  <div class="tile-label">PAVING</div>
</div>
<div class="tile" style="left:864px;top:1858px;width:238px;height:182px">
  <div class="photo" role="img" aria-label="Blue swimming pool in a green lawn" style="inset:0;background:linear-gradient(180deg,#8fb4d8,#3ca3dc 45%,#5a8e3a)"></div>
  <div class="tile-label">SWIMMING POOLS</div>
</div>
<div class="tile" style="left:100px;top:2060px;width:492px;height:178px">
  <div class="photo" role="img" aria-label="Stone fire table filled with blue glass stones" style="inset:0;background:linear-gradient(180deg,#cfc8bd,#a79c8c 40%,#3e5a9a 55%,#6a6058)"></div>
  <div class="tile-label">MARBLES BLUE STONES</div>
</div>
<div class="tile" style="left:864px;top:2060px;width:238px;height:178px">
  <div class="photo" role="img" aria-label="Warmly lit indoor spa with stone walls" style="inset:0;background:linear-gradient(180deg,#3a2a1c,#8a6a3e 50%,#5a4a3a)"></div>
  <div class="tile-label">SPAS</div>
</div>
<div class="btn" style="left:548px;top:2270px;width:104px">VIEW ALL</div>

<section class="partners">
  <h2 class="section-title" style="top:38px">WE WORK <span class="soft">WITH</span></h2>
  <svg class="divider" style="top:82px" viewBox="0 0 170 22"><line x1="0" y1="11" x2="70" y2="11" stroke="#bbb"/><line x1="100" y1="11" x2="170" y2="11" stroke="#bbb"/><path d="M78 18h14V8l-7-5-7 5z" fill="var(--blue)"/></svg>
  <div class="partner" style="left:100px"><span class="dot round"></span>ORBEL</div>
  <div class="partner" style="left:362px">loam properties</div>
  <div class="partner" style="left:626px"><span class="dot"></span>DRV</div>
  <div class="partner" style="left:890px">quill construction</div>
</section>

<footer class="site-footer">
  <div class="foot-h" style="left:100px">QUICK LINKS</div>
  <ul class="quick"><li>Home</li><li>About Us</li><li>Services</li><li>Our Work</li><li>Contact Us</li></ul>

  <div class="foot-h" style="left:320px">CONTACT DETAILS</div>
  <div class="contact">
    <div class="row"><svg width="12" height="16" viewBox="0 0 12 16"><path d="M6 0a6 6 0 0 1 6 6c0 4-6 10-6 10S0 10 0 6a6 6 0 0 1 6-6z" fill="#fff"/><circle cx="6" cy="6" r="2.2" fill="#2f2f2f"/></svg><div><strong>TALL WAVE CONSTRUCTION</strong><br>123 Lorem ipsum dolor sit amet,<br>consectetuer adipiscing elit.</div></div>
    <div class="row"><svg width="14" height="14" viewBox="0 0 24 24"><path fill="#fff" d="M6.6 10.8a15 15 0 0 0 6.6 6.6l2.2-2.2c.3-.3.7-.4 1-.2 1.1.4 2.3.6 3.6.6.6 0 1 .4 1 1V20c0 .6-.4 1-1 1A17 17 0 0 1 3 4c0-.6.4-1 1-1h3.5c.6 0 1 .4 1 1 0 1.3.2 2.5.6 3.6.1.3 0 .7-.2 1z"/></svg><div>555-014-2290</div></div>
    <div class="row"><svg width="14" height="14" viewBox="0 0 14 14"><rect x="3" y="0" width="8" height="4" fill="#fff"/><rect x="0" y="4" width="14" height="6" fill="#fff"/><rect x="3" y="9" width="8" height="5" fill="#fff" stroke="#2f2f2f"/></svg><div>555-014-2290</div></div>
    <div class="row"><svg width="14" height="14" viewBox="0 0 24 24"><path fill="#fff" d="M2 5h20v14H2zm2 2v.5l8 5 8-5V7l-8 5z"/></svg><div>hello@tallwave.example</div></div>
  </div>

  <div class="foot-h" style="left:630px">LOCATION MAP</div>
  <div class="map" role="img" aria-label="Road map of the service area"></div>

  <div class="foot-brand">
    <span class="brand-mark"></span>
    <div class="brand-name">Tall Wave</div>
    <div class="brand-sub">CONSTRUCTION</div>
    <div class="foot-socials"><span></span><span></span><span></span><span></span></div>
  </div>
</footer>
<div class="copyright">Copyright © 2017 TALL WAVE CONSTRUCTION. All Rights Reserved.</div>

</body>
</html>
```